BOLD & MINIMALIST DESIGN NEEDED

We want a very bold but minimalistic business card design that is impactful and utilizes both sides of the business card. Our current logo is included for your use.

We want bold fonts and good use of negative space. We don't want the logo to overpower the design.

Target Market(s)

Professionals who are building new commercial buildings.

Industry/Entity Type

Construction

Contact Information for Business Card

Name, Title, email, office phone, cell phone, website

Font styles to use
Serif
Sans Serif

Requirements
Must have
• Bold design!

```html
<!DOCTYPE html>
<html lang="en">
<head>
<meta charset="utf-8">
<title>Ridgeline Design + Build — Business Card</title>
<link href="https://fonts.googleapis.com/css2?family=Poppins:wght@500;600;700&display=swap" rel="stylesheet">
<style>
  :root {
    --stage: #a9a9a9;
    --ink: #0e0e0e;
    --paper: #ffffff;
    --lime: #9bcf4c;
    --text-dark: #1c1c1c;
  }
  * { margin: 0; padding: 0; box-sizing: border-box; }
  html, body {
    width: 1056px; height: 1200px; overflow: hidden;
    background: var(--stage);
    font-family: "Poppins", Arial, sans-serif;
  }
  .card {
    position: absolute; left: 113px; width: 829px; height: 474px;
    overflow: hidden;
    box-shadow: 0 6px 22px rgba(0,0,0,0.28);
  }
  .card--front { top: 86px; background: var(--ink); }
  .card--back { top: 624px; background: var(--paper); }

  .side-tab {
    position: absolute; top: 158px; width: 15px; height: 220px;
    background: var(--lime);
  }
  .side-tab--left { left: 0; border-radius: 0 40px 40px 0; }
  .side-tab--right { right: 0; border-radius: 40px 0 0 40px; }

  .brand {
    position: absolute; left: 0; right: 0;
    display: flex; align-items: center; justify-content: center; gap: 12px;
    font-weight: 700; font-size: 30px; letter-spacing: 1px; text-transform: uppercase;
  }
  .brand__mark { width: 18px; height: 18px; background: var(--lime); }
  .card--front .brand { top: 180px; color: var(--paper); }
  .card--back .brand { top: 128px; color: var(--text-dark); }

  .front-web {
    position: absolute; left: 0; right: 0; top: 346px;
    text-align: center; color: var(--paper);
    font-weight: 600; font-size: 28px; letter-spacing: 3px;
  }
  .front-web .accent { color: var(--lime); }

  .contact {
    position: absolute; display: flex; align-items: flex-start; gap: 11px;
    color: var(--text-dark); font-weight: 500; font-size: 22px; line-height: 28px;
  }
  .contact__icon {
    flex: none; width: 26px; height: 26px; border-radius: 50%;
    background: var(--lime); display: flex; align-items: center; justify-content: center;
    margin-top: 1px;
  }
  .contact__icon svg { width: 14px; height: 14px; }
  .contact--phone { left: 121px; top: 284px; }
  .contact--address { left: 121px; top: 328px; }
  .contact--email { left: 471px; top: 284px; }
  .contact--web { left: 471px; top: 353px; }

  .base-bar {
    position: absolute; left: 323px; right: 0; bottom: 0; height: 17px;
    background: var(--lime); border-radius: 17px 0 0 0;
  }
</style>
</head>
<body>

<section class="card card--front">
  <div class="side-tab side-tab--left"></div>
  <div class="side-tab side-tab--right"></div>
  <div class="brand"><span class="brand__mark"></span>Ridgeline Design + Build</div>
  <p class="front-web">www.<span class="accent">r-d-b</span>.com</p>
</section>

<section class="card card--back">
  <div class="brand"><span class="brand__mark"></span>Ridgeline Design + Build</div>

  <div class="contact contact--phone">
    <span class="contact__icon">
      <svg viewBox="0 0 24 24"><path fill="#1c1c1c" d="M6.6 10.8a15.1 15.1 0 0 0 6.6 6.6l2.2-2.2a1 1 0 0 1 1-.25 11.4 11.4 0 0 0 3.6.57 1 1 0 0 1 1 1V20a1 1 0 0 1-1 1A17 17 0 0 1 3 4a1 1 0 0 1 1-1h3.5a1 1 0 0 1 1 1c0 1.25.2 2.45.57 3.57a1 1 0 0 1-.25 1z"/></svg>
    </span>
    <span>555-014-2200</span>
  </div>

  <div class="contact contact--address">
    <span class="contact__icon">
      <svg viewBox="0 0 24 24"><path fill="#1c1c1c" d="M12 2a7 7 0 0 0-7 7c0 5.25 7 13 7 13s7-7.75 7-13a7 7 0 0 0-7-7zm0 9.5A2.5 2.5 0 1 1 12 6.5a2.5 2.5 0 0 1 0 5z"/></svg>
    </span>
    <span>4120 Cedar Hollow Rd.<br>Pine Ridge, GA 30999</span>
  </div>

  <div class="contact contact--email">
    <span class="contact__icon">
      <svg viewBox="0 0 24 24"><rect x="2" y="5" width="20" height="14" rx="1.5" fill="#1c1c1c"/><path d="M3 6l9 7 9-7" stroke="#9bcf4c" stroke-width="1.6" fill="none"/></svg>
    </span>
    <span>info@r-d-b.com</span>
  </div>

  <div class="contact contact--web">
    <span class="contact__icon">
      <svg viewBox="0 0 24 24" fill="none" stroke="#1c1c1c" stroke-width="1.8"><circle cx="12" cy="12" r="9"/><ellipse cx="12" cy="12" rx="4" ry="9"/><path d="M3 12h18M4.5 7.5h15M4.5 16.5h15"/></svg>
    </span>
    <span>www.r-d-b.com</span>
  </div>

  <div class="base-bar"></div>
</section>

</body>
</html>
```